Professional & Modern Technology Business Card

We need a business card for our software/technology firm. Our services include Program/Project Management, Project Controls and Enterprise Analytics. Our clients are usually in the Aviation, Public Works, Transportation and Electric & Water Utility industries. We serve both public and private clients. Would like a very professional, conservative but somewhat modern design. Design, Develop, Deploy is the corporate tagline. We have two offices. The headquarters is in Atlanta, GA and a satellite office In Savannah, GA. Corporate Logo Attached.
Looking to do website and corporate brochure after the successful completion of this project. Would like to begin a working relationship with best designers.
Tagline: Design, Develop, Deploy
Website: www.quambelsystems.example
My Name: Delia Marchetti
My Title: CEO
Email: dmarchetti@quambelsystems.example
Atlanta Address:
87 Corliss Avenue, #2260
Atlanta, GA 30301
Office: 404.555.0178
Fax: 404.555.0143
Mobile: 404.555.0116
Savannah Address:
315 West Harrow Lane Street
Suite 720
Savannah, GA 31401
Office: 912.555.0162
Fax: 404.555.0143
Mobile: 404.555.0116
Please include the email address in your designs: dmarchetti@quambelsystems.example.
I appreciate everyone's design efforts. Just a few notes:
1. Please remove the mobile number from the cards
2. The backs of the cards can be utilized for writing notes. Make sure your design on the back of the card is conducive to clearly adding writing if needed.
3. No black backgrounds please
4. Only use the corporate logo on the front of the card. You can use portions of the logo design, but not the logo in totality.
Thank You
Conservative

```html
<!DOCTYPE html>
<html lang="en">
<head>
<meta charset="utf-8">
<title>Quambel Systems – Business Card</title>
<link rel="stylesheet" href="https://fonts.googleapis.com/css2?family=Mulish:wght@400;700&display=swap">
<style>
  :root {
    --bg: #e9ebee;
    --card: #ffffff;
    --brand-blue: #0a8fd6;
    --ink: #2b2b2b;
    --ink-soft: #555555;
    --muted: #8a8a8a;
    --rule: #e3e3e3;
    --dot: #e9b90f;
  }
  * { box-sizing: border-box; margin: 0; padding: 0; }
  html, body { width: 1200px; height: 1000px; overflow: hidden; }
  body {
    background: var(--bg);
    font-family: "Mulish", "Century Gothic", sans-serif;
    color: var(--ink);
    position: relative;
  }
  .card {
    position: absolute;
    left: 250px;
    width: 700px;
    height: 400px;
    background: var(--card);
    box-shadow: 0 10px 30px rgba(0,0,0,.12);
  }
  .card-back {
    top: 50px;
    clip-path: polygon(70px 0, 100% 0, 100% 78%, 620px 100%, 0 100%, 0 70px);
  }
  .card-front {
    top: 540px;
    clip-path: polygon(0 0, 630px 0, 100% 70px, 100% 100%, 80px 100%, 0 310px);
  }
  /* back */
  .notes-label {
    position: absolute; left: 70px; top: 52px;
    font-weight: 700; font-size: 22px; color: var(--ink);
  }
  .note-lines { position: absolute; left: 60px; top: 80px; width: 540px; }
  .note-line { height: 46px; border-bottom: 1.5px solid var(--rule); }
  .note-line:first-child { margin-left: 90px; }
  .tagline {
    position: absolute; right: 30px; top: 36px;
    writing-mode: vertical-rl; transform: rotate(180deg);
    white-space: nowrap;
    font-size: 19px; letter-spacing: 1px; color: var(--ink-soft);
  }
  .back-web {
    position: absolute; left: 64px; bottom: 28px;
    font-size: 20px; color: var(--muted); letter-spacing: .5px;
    white-space: nowrap;
  }
  /* front */
  .brand {
    position: absolute; left: 42px; top: 38px;
    display: flex; align-items: center; gap: 12px;
  }
  .brand-dot { width: 46px; height: 46px; border-radius: 50%; background: var(--dot); flex: none; }
  .brand-name { font-size: 26px; font-weight: 700; color: var(--ink); line-height: 1.05; }
  .front-web {
    position: absolute; right: 40px; top: 38px;
    font-size: 17px; color: var(--muted); letter-spacing: .5px;
    white-space: nowrap;
  }
  .name-band {
    position: absolute; left: 0; right: 0; top: 118px; height: 92px;
    background: var(--brand-blue); color: #fff;
    padding: 14px 0 0 42px;
  }
  .person-name { font-size: 28px; font-weight: 700; }
  .person-title { font-size: 20px; font-weight: 400; margin-left: 8px; }
  .person-email { font-size: 21px; margin-top: 2px; }
  .office { position: absolute; font-size: 18px; line-height: 1.25; color: var(--ink-soft); white-space: nowrap; }
  .office h2 { font-size: 18px; font-weight: 700; color: var(--ink); }
  .office-atlanta { left: 110px; top: 232px; }
  .office-savannah { left: 420px; top: 232px; }
  .office .lines { margin-bottom: 8px; }
</style>
</head>
<body>

<section class="card card-back" aria-label="Card back">
  <p class="notes-label">Notes:</p>
  <div class="note-lines">
    <div class="note-line"></div>
    <div class="note-line"></div>
    <div class="note-line"></div>
    <div class="note-line"></div>
    <div class="note-line"></div>
  </div>
  <p class="tagline">Design | Develop | Deploy</p>
  <p class="back-web">www.quambelsystems.example</p>
</section>

<section class="card card-front" aria-label="Card front">
  <div class="brand">
    <span class="brand-dot"></span>
    <span class="brand-name">Quambel<br>Systems, Inc.</span>
  </div>
  <p class="front-web">www.quambelsystems.example</p>
  <div class="name-band">
    <p><span class="person-name">Delia Marchetti</span><span class="person-title">- C.E.O</span></p>
    <p class="person-email">dmarchetti@quambelsystems.example</p>
  </div>
  <div class="office office-atlanta">
    <h2>Atlanta Address:</h2>
    <p class="lines">87 Corliss Avenue, #2260<br>Atlanta, GA 30301</p>
    <p>T: 404 555 0178<br>F: 404 555 0143</p>
  </div>
  <div class="office office-savannah">
    <h2>Savannah Address:</h2>
    <p class="lines">315 West Harrow Lane Street<br>Suite 720<br>Savannah, GA 31401</p>
    <p>T: 912 555 0162<br>F: 404 555 0143</p>
  </div>
</section>

</body>
</html>
```